Company Marketing Flyers for SEO company

Marlowe Reach Bureau requires a four page A4 color brochure for small businesses who are being marketed to for SEO services.

The brochure is provided to the potential client during a first meeting. So we are looking for nice glossy pictures combined with sufficient text to enable the applicant to make an informed decision.

I have attached a word document that contains the text that may help plus lots of pictures that are on the website that could be used also.

Target Market(s)

small businesses seeking SEO support and assistance

Industry/Entity Type

Marketing

Font styles to use
Sans Serif

Colors
9bcb3c
0555a3
acd036
cadf82
eaf2ce
ffffff

Requirements
Must have
• color photos, glossy, exciting and fun
Nice to have
• happy, quality
Should not have
• scary stuff

```html
<!DOCTYPE html>
<html lang="en">
<head>
<meta charset="utf-8">
<title>Marlowe Reach Bureau – Brochure Spread</title>
<link rel="stylesheet" href="https://fonts.googleapis.com/css2?family=Open+Sans:wght@300;400;600;700&display=swap">
<style>
  :root {
    --green: #9bcb3c;
    --green-deep: #5cb531;
    --lime: #acd036;
    --sage: #cadf82;
    --mist: #eaf2ce;
    --white: #ffffff;
    --ink: #3c3c3c;
    --ink-soft: #6a6a6a;
    --backdrop: #e4e4e4;
  }
  * { box-sizing: border-box; margin: 0; padding: 0; }
  html, body { width: 1200px; height: 900px; overflow: hidden; }
  body {
    background: var(--backdrop);
    font-family: "Open Sans", sans-serif;
    color: var(--ink);
  }
  .spread {
    position: absolute;
    left: 49px; top: 60px;
    width: 1102px; height: 780px;
    display: flex;
    box-shadow: 0 10px 30px rgba(0,0,0,.15);
  }
  .page {
    position: relative;
    width: 551px; height: 780px;
    background: var(--white);
    overflow: hidden;
  }
  .page--left { background: linear-gradient(90deg, #f7f7f7, #ececec); }
  .page--right { background: linear-gradient(90deg, #ededed, #f9f9f9); }

  /* Left page */
  .office-photo {
    position: absolute; left: 34px; top: 34px;
    width: 500px; height: 290px;
    background: linear-gradient(160deg, #e9e2d6 0%, #c9b89c 40%, #8a7a56 70%, #ddd6c8 100%);
  }
  .chat-badge {
    position: absolute; left: 22px; top: 255px;
    width: 110px; height: 110px;
  }
  .info-block {
    position: absolute; left: 40px; top: 385px; width: 420px;
  }
  .info-title {
    color: var(--green-deep);
    font-size: 21px; font-weight: 400;
    letter-spacing: .5px;
    margin-bottom: 14px;
  }
  .body-copy {
    font-size: 10.5px; line-height: 1.45;
    margin-bottom: 10px;
    text-align: justify;
  }
  .body-copy strong { font-weight: 700; }
  .address { font-size: 10.5px; line-height: 1.45; margin-bottom: 10px; }
  .contact-list { list-style: none; margin-top: 22px; }
  .contact-list li {
    display: flex; align-items: center; gap: 10px;
    font-size: 12px; margin-bottom: 10px;
  }
  .contact-list svg { width: 14px; height: 14px; }

  .brand {
    position: absolute; right: 40px; bottom: 40px;
    display: flex; align-items: center; gap: 10px;
    padding-top: 12px;
    border-top: 1px solid var(--green);
  }
  .brand-dot { width: 14px; height: 14px; border-radius: 50%; background: var(--green-deep); }
  .brand-name {
    font-size: 22px; font-weight: 300; color: var(--green-deep);
  }

  /* Right page */
  .tablet-photo {
    position: absolute; left: 18px; top: 34px;
    width: 500px; height: 420px;
    background: linear-gradient(135deg, #a9713f 0%, #c7925c 35%, #e9e6d6 55%, #7a5434 85%);
  }
  .section-tag {
    position: absolute; left: 40px; top: 20px;
    width: 150px; height: 120px;
    background: rgba(92,181,49,.82);
    color: var(--white);
    font-size: 20px; font-weight: 300; line-height: 1.15;
    letter-spacing: 1px;
    padding: 20px 16px;
    text-transform: uppercase;
  }
  .services-block {
    position: absolute; left: 40px; top: 476px; width: 340px;
  }
  .services-block .body-copy { font-size: 9.5px; margin-bottom: 8px; }
  .highlight { color: var(--green-deep); font-weight: 700; }
  .web-link {
    color: var(--green-deep); font-size: 12px; font-weight: 600;
    margin-top: 6px;
  }
</style>
</head>
<body>
  <div class="spread">
    <section class="page page--left">
      <div class="office-photo" role="img" aria-label="Photo of a smiling young woman leaning on a desk in a bright office, colleagues in the background"></div>

      <svg class="chat-badge" viewBox="0 0 110 110" aria-hidden="true">
        <polygon points="55,2 103,28 103,82 55,108 7,82 7,28" fill="#5cb531" opacity=".92"/>
        <path d="M30 38 h30 a8 8 0 0 1 8 8 v14 a8 8 0 0 1 -8 8 h-20 l-10 9 v-9 a8 8 0 0 1 -8 -8 v-14 a8 8 0 0 1 8 -8z" fill="none" stroke="#fff" stroke-width="4"/>
        <path d="M72 48 h6 a8 8 0 0 1 8 8 v12 a8 8 0 0 1 -8 8 v8 l-9 -8 h-14" fill="none" stroke="#fff" stroke-width="4"/>
      </svg>

      <div class="info-block">
        <h2 class="info-title">FOR MORE INFORMATION</h2>
        <p class="body-copy"><strong>Marlowe Reach Bureau</strong> was established on 18 November 2015 to assist businesses around Australia integrate proven internet marketing techniques and help them grow inbound enquiries, online sales and provide greater solutions to existing and future clients.</p>
        <p class="body-copy">Marlowe Reach Bureau has an intimate understanding of <strong>Search Engine Optimisation (SEO), Pay per Click (PPC), Social Media Optimisation (SMO), online advertising</strong> and building business brands across Australia that compete with large organisations and take from them market share.</p>
        <p class="address"><strong>Marlowe Reach Bureau</strong><br>Level 9, 210 Harbour Lane<br>Melbourne VIC 3000</p>
        <p class="address">Level 6, 41 Keel Street<br>Sydney NSW 2000</p>
        <ul class="contact-list">
          <li>
            <svg viewBox="0 0 14 14" aria-hidden="true"><circle cx="7" cy="7" r="7" fill="#5cb531"/><path d="M4.5 3.5 l1.5 0 .6 1.8 -1 .8 a5 5 0 0 0 2.3 2.3 l.8 -1 1.8 .6 0 1.5 a1 1 0 0 1 -1 1 A6 6 0 0 1 3.5 4.5 a1 1 0 0 1 1 -1z" fill="#fff"/></svg>
            1300 48 27 05
          </li>
          <li>
            <svg viewBox="0 0 14 14" aria-hidden="true"><circle cx="7" cy="7" r="7" fill="#5cb531"/><rect x="3.5" y="4.5" width="7" height="5" fill="#fff"/><path d="M3.5 4.5 L7 7.3 L10.5 4.5" fill="none" stroke="#5cb531" stroke-width=".8"/></svg>
            info@marlowereach.com.au
          </li>
        </ul>
      </div>

      <div class="brand">
        <span class="brand-dot"></span>
        <span class="brand-name">Marlowe Reach Bureau</span>
      </div>
    </section>

    <section class="page page--right">
      <div class="tablet-photo" role="img" aria-label="Photo of hands using a tablet showing an online marketing sketch, with glasses, a plant and chart notes on a wooden desk"></div>
      <div class="section-tag">Online<br>Marketing<br>Tools</div>

      <div class="services-block">
        <p class="body-copy"><strong>Marlowe Reach Bureau</strong> works with organisations to design, implement and oversee an <strong>online marketing</strong>, Search Engine Optimisation (SEO), Social Media Optimisation (SMO) and Search Engine Marketing (SEM) strategy. Integral to the strategy is getting your website <span class="highlight">ranking high on the major search engines</span> to increase site visitors and then boost conversions into leads and sales.</p>
        <p class="body-copy">We aim to give your business the tools to hit your competition hard and take from them market share across each product and service offering.</p>
        <p class="body-copy">Comprehensive <strong>Small Business SEO</strong> package fees from <strong>$1,800.00 per month</strong> plus GST.</p>
        <p class="web-link">www.marlowereach.com.au</p>
      </div>

      <div class="brand">
        <span class="brand-dot"></span>
        <span class="brand-name">Marlowe Reach Bureau</span>
      </div>
    </section>
  </div>
</body>
</html>
```